Female Pest Controller needs awesome business cards

I need a logo design for a Pest Control service - something that appeals to 'nature' & safe, with the use of the colour green. I am also female
New Business Name is 'Bug Bolted'
appeals to women

Target Market(s)

Domestic Households & Local Businesses

Industry/Entity Type

Pest Control

Contact Information for Business Card

Rowena Calderitt
0438526190
ABN 61 847 530 218
PMT7309145538
Spiders Cockroaches, Ants, Silverfish, Fleas, Rodents

Font styles to use
Decorative

Colors
abd036
aaaaaa
5c5c5c

Requirements
Should not have
• Pics of dead insects, prefer nature inspired designs, frogs, trees etc
• Have attached old log & business name ( now my ex's business) Brookhaven Pest Solutions -

```html
<!DOCTYPE html>
<html lang="en">
<head>
<meta charset="utf-8">
<title>Bug Bolted – Business Card</title>
<link href="https://fonts.googleapis.com/css2?family=Open+Sans:wght@400;700&display=swap" rel="stylesheet">
<style>
  :root {
    --green: #abd036;
    --grey-light: #aaaaaa;
    --grey-dark: #5c5c5c;
    --card: #ffffff;
    --backdrop: #ecebe8;
  }
  html, body {
    margin: 0;
    width: 1200px;
    height: 900px;
    overflow: hidden;
    background: var(--backdrop);
    font-family: "Open Sans", Arial, sans-serif;
  }
  .business-card {
    position: absolute;
    left: 150px;
    top: 175px;
    width: 900px;
    height: 550px;
    background: var(--card);
    box-shadow: 0 6px 24px rgba(0,0,0,0.12);
    overflow: hidden;
  }
  .edge-band-bottom {
    position: absolute;
    left: 0;
    right: 0;
    bottom: 0;
    height: 16px;
    background: var(--grey-dark);
  }
  .edge-band-right {
    position: absolute;
    right: 0;
    top: 250px;
    bottom: 0;
    width: 14px;
    background: var(--grey-dark);
  }
  .tree-canopy {
    position: absolute;
    right: 0;
    top: 0;
    width: 190px;
    height: 275px;
    background: var(--green);
    border-bottom-left-radius: 90px 120px;
    border-top-left-radius: 60px 80px;
  }
  .brand {
    position: absolute;
    left: 70px;
    top: 262px;
    display: flex;
    align-items: center;
    gap: 12px;
  }
  .brand-dot {
    width: 26px;
    height: 26px;
    border-radius: 50%;
    background: var(--green);
  }
  .brand-name {
    font-size: 44px;
    font-weight: 400;
    color: var(--grey-dark);
    letter-spacing: 0.5px;
    line-height: 1;
  }
  .contact {
    position: absolute;
    left: 72px;
    top: 338px;
    color: var(--grey-dark);
  }
  .contact-name {
    margin: 0;
    font-size: 22px;
    font-weight: 700;
    text-transform: uppercase;
    letter-spacing: 0.3px;
  }
  .contact-phone {
    margin: 2px 0 6px;
    display: flex;
    align-items: center;
    gap: 8px;
    font-size: 34px;
    font-weight: 700;
    line-height: 1.1;
  }
  .contact-phone svg { width: 24px; height: 24px; }
  .contact-line {
    margin: 0;
    padding-left: 22px;
    font-size: 19px;
    font-weight: 400;
    line-height: 1.35;
  }
</style>
</head>
<body>
  <main class="business-card">
    <div class="tree-canopy" role="img" aria-label="Green tree foliage silhouette along the right edge"></div>
    <div class="edge-band-right"></div>
    <div class="edge-band-bottom"></div>

    <div class="brand">
      <span class="brand-dot"></span>
      <span class="brand-name">Bug Bolted</span>
    </div>

    <section class="contact">
      <p class="contact-name">Rowena Calderitt</p>
      <p class="contact-phone">
        <svg viewBox="0 0 24 24" aria-hidden="true">
          <circle cx="12" cy="12" r="10.5" fill="none" stroke="#5c5c5c" stroke-width="2"/>
          <path d="M8.6 6.8c.4-.3 1-.2 1.2.3l1 2c.2.4.1.8-.2 1.1l-.7.6c.6 1.3 1.6 2.4 2.9 3l.6-.7c.3-.3.8-.4 1.1-.2l2 1c.5.2.6.8.3 1.2l-.8 1.1c-.4.5-1 .7-1.6.5-3.3-1-5.9-3.6-6.8-6.9-.2-.6 0-1.2.5-1.6z" fill="#5c5c5c"/>
        </svg>
        0438526190
      </p>
      <p class="contact-line">ABN 61 847 530 218</p>
      <p class="contact-line">PMT Lic:</p>
      <p class="contact-line">Spiders Cockroaches, Ants, Silverfish, Fleas, Rodents</p>
    </section>
  </main>
</body>
</html>
```